Package design for Mica powder sachets

Our mica powder product comes in two sets of colors, a set of 60 and 35 packed inside sachet bags individually. This project will require two sizes of the packing box , one for the set of 60 and other for 35. We do not have a specific design requirement as long as the design reflects the theme of our product. Box diagram for both sizes is attached together with color chart, content, logo, sachet design and sample of a packaging design we like. The content is the same for both sizes accept for number of colors included.

```html
<!DOCTYPE html>
<html lang="en">
<head>
<meta charset="UTF-8">
<title>Birch Studio – Mica Powder 35 Colors – Box Dieline</title>
<link rel="stylesheet" href="https://fonts.googleapis.com/css2?family=Montserrat:wght@300;400;500;700&display=swap">
<style>
  :root {
    --page-bg: #ffffff;
    --panel: #111111;
    --fold: #9a9a9a;
    --ink: #ffffff;
    --ink-soft: #d9d9d9;
    --frame: #cfcfcf;
  }
  html, body {
    margin: 0;
    padding: 0;
    width: 1200px;
    height: 707px;
    overflow: hidden;
    background: var(--page-bg);
  }
  .dieline {
    position: absolute;
    left: 222px;
    top: 10px;
    width: 756px;
    height: 686px;
    display: block;
  }
  .panel { fill: var(--panel); }
  .fold { stroke: var(--fold); stroke-width: 1.5; fill: none; }
  .brand {
    font-family: "Montserrat", sans-serif;
    font-weight: 500;
    fill: var(--ink);
  }
  .side-label {
    font-family: "Montserrat", sans-serif;
    font-weight: 700;
    font-size: 19px;
    fill: var(--ink);
    letter-spacing: 1px;
  }
  .product-title {
    font-family: "Montserrat", sans-serif;
    font-weight: 300;
    font-size: 29px;
    fill: var(--ink);
  }
  .product-count {
    font-family: "Montserrat", sans-serif;
    font-weight: 700;
    font-size: 19px;
    fill: var(--ink);
  }
  .product-detail {
    font-family: "Montserrat", sans-serif;
    font-weight: 400;
    font-size: 11px;
    fill: var(--ink-soft);
  }
  .color-list {
    font-family: "Montserrat", sans-serif;
    font-weight: 400;
    font-size: 7.5px;
    fill: var(--ink-soft);
    letter-spacing: 0.3px;
  }
  .list-frame { fill: none; stroke: var(--frame); stroke-width: 1.2; }
  .list-divider { stroke: var(--frame); stroke-width: 0.8; }
</style>
</head>
<body>
<svg class="dieline" viewBox="1134 157 1260 1143" xmlns="http://www.w3.org/2000/svg">
  <defs>
    <linearGradient id="powder-tones" x1="0" y1="0" x2="1" y2="1">
      <stop offset="0" stop-color="#e83f7a"/>
      <stop offset="0.3" stop-color="#f2a23a"/>
      <stop offset="0.55" stop-color="#2e4fc9"/>
      <stop offset="0.8" stop-color="#2f9e4a"/>
      <stop offset="1" stop-color="#e4482f"/>
    </linearGradient>
    <linearGradient id="powder-fade" x1="0" y1="0" x2="1" y2="0">
      <stop offset="0" stop-color="#111111" stop-opacity="1"/>
      <stop offset="0.35" stop-color="#111111" stop-opacity="0"/>
    </linearGradient>
  </defs>

  <!-- top lid flap row -->
  <g class="lid-flap-row">
    <rect class="panel" x="1370" y="161" width="157" height="164"/>
    <rect class="panel" x="1528" y="157" width="471" height="170"/>
    <rect class="panel" x="2001" y="161" width="156" height="164"/>
    <text class="brand" font-size="22" text-anchor="middle" transform="rotate(180 1763 242)" x="1763" y="250">Birch Studio</text>
  </g>

  <!-- lid row -->
  <g class="lid-row">
    <rect class="panel" x="1134" y="330" width="196" height="312"/>
    <rect class="panel" x="1331" y="330" width="196" height="312"/>
    <rect class="panel" x="1528" y="330" width="471" height="312"/>
    <rect class="panel" x="2001" y="330" width="195" height="312"/>
    <rect class="panel" x="2197" y="330" width="196" height="312"/>
    <text class="side-label" text-anchor="middle" transform="rotate(90 1433 478)" x="1433" y="485">35 COLORS</text>
    <text class="side-label" text-anchor="middle" transform="rotate(-90 2098 478)" x="2098" y="485">35 COLORS</text>

    <g class="color-chart" transform="rotate(180 1764 488)">
      <rect class="list-frame" x="1572" y="388" width="384" height="200"/>
      <text class="brand" font-size="22" text-anchor="middle" x="1764" y="440">Birch Studio</text>
      <line class="list-divider" x1="1667" y1="478" x2="1667" y2="574"/>
      <line class="list-divider" x1="1763" y1="478" x2="1763" y2="574"/>
      <line class="list-divider" x1="1859" y1="478" x2="1859" y2="574"/>
      <text class="color-list" x="1590" y="486">
        <tspan x="1590" dy="0">SAGE GLOW</tspan><tspan x="1590" dy="9.5">PEARL WHITE</tspan><tspan x="1590" dy="9.5">LIGHT GOLD</tspan><tspan x="1590" dy="9.5">YELLOW GOLD</tspan><tspan x="1590" dy="9.5">CLASSIC GOLD</tspan><tspan x="1590" dy="9.5">GLITZY GOLD</tspan><tspan x="1590" dy="9.5">CITRUS ZEST</tspan><tspan x="1590" dy="9.5">LEMON TWIST</tspan><tspan x="1590" dy="9.5">CHARCOAL</tspan>
      </text>
      <text class="color-list" x="1680" y="486">
        <tspan x="1680" dy="0">SPACE GRAY</tspan><tspan x="1680" dy="9.5">CHOCOLATE BROWN</tspan><tspan x="1680" dy="9.5">BRONZE</tspan><tspan x="1680" dy="9.5">GOLDEN BROWN</tspan><tspan x="1680" dy="9.5">JUNGLE GREEN</tspan><tspan x="1680" dy="9.5">TURQUOISE</tspan><tspan x="1680" dy="9.5">MINT GREEN</tspan><tspan x="1680" dy="9.5">EMERALD GREEN</tspan><tspan x="1680" dy="9.5">SPRING GREEN</tspan>
      </text>
      <text class="color-list" x="1776" y="486">
        <tspan x="1776" dy="0">SKY BLUE</tspan><tspan x="1776" dy="9.5">DENIM BLUE</tspan><tspan x="1776" dy="9.5">BRIGHT BLUE</tspan><tspan x="1776" dy="9.5">SAPPHIRE BLUE</tspan><tspan x="1776" dy="9.5">NAVY BLUE</tspan><tspan x="1776" dy="9.5">VIOLET PURPLE</tspan><tspan x="1776" dy="9.5">LAVENDER</tspan><tspan x="1776" dy="9.5">CORAL ORANGE</tspan><tspan x="1776" dy="9.5">ROSE RED</tspan>
      </text>
      <text class="color-list" x="1872" y="486">
        <tspan x="1872" dy="0">RASPBERRY</tspan><tspan x="1872" dy="9.5">ROSE PINK</tspan><tspan x="1872" dy="9.5">HOT PINK</tspan><tspan x="1872" dy="9.5">CREAM PINK</tspan><tspan x="1872" dy="9.5">BURGUNDY</tspan><tspan x="1872" dy="9.5">COPPER</tspan><tspan x="1872" dy="9.5">BRONZE GOLD</tspan><tspan x="1872" dy="9.5">BRILLIANT SILVER</tspan>
      </text>
    </g>
  </g>

  <!-- back wall row -->
  <g class="back-row">
    <rect class="panel" x="1370" y="647" width="157" height="164"/>
    <rect class="panel" x="1528" y="645" width="471" height="166"/>
    <rect class="panel" x="2001" y="647" width="156" height="164"/>
    <text class="brand" font-size="22" text-anchor="middle" transform="rotate(180 1763 728)" x="1763" y="736">Birch Studio</text>
  </g>

  <!-- front panel with dust tabs -->
  <g class="front-row">
    <path class="panel" d="M1527,815 L1390,845 Q1332,858 1332,905 L1332,1040 Q1332,1085 1390,1095 L1527,1128 Z"/>
    <path class="panel" d="M2001,815 L2138,845 Q2196,858 2196,905 L2196,1040 Q2196,1085 2138,1095 L2001,1128 Z"/>
    <rect class="panel" x="1528" y="815" width="471" height="313"/>
    <g role="img" aria-label="Photograph of a model's profile covered in glowing multicoloured mica powder">
      <rect x="1780" y="815" width="219" height="313" fill="url(#powder-tones)"/>
      <rect x="1780" y="815" width="219" height="313" fill="url(#powder-fade)"/>
    </g>
    <text class="brand" font-size="34" x="1565" y="905">Birch Studio</text>
    <text class="product-title" x="1562" y="1011">MICA POWDER</text>
    <text class="product-count" x="1564" y="1056">35 COLORS</text>
    <text class="product-detail" x="1564" y="1073">multi-propose | cosmetic grade | non-toxic</text>
    <text class="product-detail" x="1564" y="1090">35 x 0.18oz (5g) | 0.2g measurement spoon</text>
  </g>

  <!-- base row -->
  <g class="base-row">
    <path class="panel" d="M1527,1130 L1365,1130 Q1328,1130 1336,1170 Q1370,1275 1470,1298 L1527,1298 Z"/>
    <path class="panel" d="M2001,1130 L2163,1130 Q2200,1130 2192,1170 Q2158,1275 2058,1298 L2001,1298 Z"/>
    <rect class="panel" x="1528" y="1130" width="471" height="168"/>
    <text class="brand" font-size="20" text-anchor="middle" x="1763" y="1218">Birch Studio</text>
  </g>

  <!-- fold lines -->
  <g class="fold">
    <line x1="1528" y1="157" x2="1528" y2="1298"/>
    <line x1="2000" y1="157" x2="2000" y2="1298"/>
    <line x1="1331" y1="330" x2="1331" y2="642"/>
    <line x1="2197" y1="330" x2="2197" y2="642"/>
    <line x1="1528" y1="328" x2="2000" y2="328"/>
    <line x1="1528" y1="643" x2="2000" y2="643"/>
    <line x1="1528" y1="813" x2="2000" y2="813"/>
    <line x1="1528" y1="1129" x2="2000" y2="1129"/>
  </g>
</svg>
</body>
</html>
```